PowerPoint Template for Consultancy Company.

We need a Power Point template for a Consultancy company based in Copenhagen, Denmark. We focus on supporting people and small companies in starting up next generation technology companies. Company name is "Vorstrup-Kjær Consulting". The template shall demonstrate growth, agility, next generation technology and following your dreams. Please include the uploaded logo.
Updates
Hi guys,
thanks for helping me on this project.
I like the font "Good Times" that is being used in my logo. I will like this to be used as minimum in the headlines in my power point template. I am not sure if it will work on standard text - but will relay on your judgement.
Kind regards
Torlak
Colors
Designer to choose colors to be used in the design.
Look and feel
Each slider illustrates characteristics of the customer's brand and the style your logo design should communicate.

```html
<!DOCTYPE html>
<html lang="en">
<head>
<meta charset="utf-8">
<title>Vorstrup-Kjær Consulting – Presentation Template</title>
<link href="https://fonts.googleapis.com/css2?family=Titillium+Web:wght@400;700&family=Open+Sans:wght@400;600&display=swap" rel="stylesheet">
<style>
:root{
  --navy:#1f2466;
  --red:#e0231f;
  --ink:#2b2b2b;
  --mid:#767170;
  --light:#bdbdbd;
  --page:#ececec;
  --white:#ffffff;
  --text:#444;
}
*{box-sizing:border-box;margin:0;padding:0}
html,body{width:1200px;height:943px;overflow:hidden;background:var(--page)}
body{position:relative;font-family:"Open Sans",sans-serif;color:var(--text)}
.slide{position:absolute;width:362px;height:203px;background:var(--white);border-top:2px solid var(--navy);border-bottom:3px solid var(--red);box-shadow:0 6px 14px rgba(0,0,0,.28);overflow:hidden}
.c1{left:34px}.c2{left:419px}.c3{left:804px}
.r1{top:35px}.r2{top:258px}.r3{top:482px}.r4{top:705px}
.abs{position:absolute}
.page-no{position:absolute;right:4px;bottom:2px;width:10px;height:10px;background:var(--red);color:#fff;font-size:6px;line-height:10px;text-align:center;font-weight:600}
.title{position:absolute;left:0;top:18px;display:flex;align-items:center;font-family:"Titillium Web",sans-serif;font-weight:700;font-size:16px;line-height:1;letter-spacing:.2px}
.title::before{content:"";width:6px;height:16px;margin-right:5px;background:currentColor}
.title.red{color:var(--red)}.title.navy{color:var(--navy)}.title.white{color:#fff}
.brand{position:absolute;display:flex;align-items:center;gap:4px;font-family:"Titillium Web",sans-serif;font-weight:700;color:var(--navy);line-height:1.05;text-transform:uppercase}
.brand .mark{background:var(--navy);flex:none}
.brand.small{top:10px;right:8px;font-size:6.5px}
.brand.small .mark{width:13px;height:13px}
.brand.light{color:#fff}.brand.light .mark{background:#fff}
.body{font-size:4.6px;line-height:1.95;color:var(--text)}
.just{text-align:justify}
.socials{position:absolute;display:flex;gap:2px}
.socials span{width:7px;height:7px;background:var(--red)}
.card{position:absolute;top:70px;width:92px;height:106px;color:#fff;text-align:center;font-size:4.5px;line-height:2.1;padding:44px 8px 0}
.card .icon{position:absolute;left:32px;top:6px;width:28px;height:26px;border:1px solid #fff}
.card svg{position:absolute;left:6px;top:5px}
.step{position:absolute;width:46px;height:45px;color:#fff;font-size:5px;text-align:center;padding-top:3px}
.step svg{display:block;margin:5px auto 0}
.goal{position:absolute;height:13px;color:#fff;font-family:"Titillium Web",sans-serif;font-weight:700;font-size:6px;letter-spacing:1.3px;text-align:center;line-height:13px}
.goal-text{position:absolute;font-size:4.4px;line-height:2.1}
.photo{position:absolute}
.frame{position:absolute;top:60px;width:70px;height:71px;padding:3px}
.frame .photo{position:relative;width:100%;height:100%}
</style>
</head>
<body>

<!-- 1 Cover -->
<section class="slide c1 r1">
  <div class="photo" role="img" aria-label="White sculpted wave surface background" style="inset:0;background:linear-gradient(100deg,#f6f6f6 0%,#e4e4e4 35%,#fafafa 55%,#dcdcdc 80%,#f3f3f3 100%)"></div>
  <div class="brand" style="left:10px;top:50px;font-size:15px;gap:8px"><span class="mark" style="width:32px;height:32px"></span><span>Vorstrup-Kjær<br>Consulting</span></div>
  <div class="abs" style="left:10px;top:99px;border:1px solid var(--navy);padding:1px 4px;font-family:'Titillium Web',sans-serif;font-weight:700;font-size:6px;letter-spacing:2px;color:var(--navy)">LEARN MORE</div>
  <div class="socials" style="right:5px;bottom:6px"><span></span><span></span><span></span><span></span></div>
</section>

<!-- 2 Quote -->
<section class="slide c2 r1">
  <div class="photo" role="img" aria-label="Black and white overhead photo of a team working at a table with papers" style="inset:0;background:radial-gradient(ellipse at 50% 50%,#9a9a9a 0%,#6a6a6a 55%,#2f2f2f 100%)"></div>
  <div class="brand light" style="left:6px;top:5px;font-size:7px"><span class="mark" style="width:14px;height:14px"></span><span>Vorstrup-Kjær<br>Consulting</span></div>
  <div class="abs" style="left:30px;top:25px;width:302px;height:150px;border:1px solid #fff"></div>
  <div class="abs" style="left:45px;top:52px;font-size:26px;color:#fff;font-family:Georgia,serif;font-weight:700">“</div>
  <p class="abs" style="left:60px;top:80px;width:230px;font-size:5.7px;line-height:1.45;color:#fff">Lorem ipsum dolor sit amet, consectetuer adipiscing elit, sed diam nonummy nibh euismod tincidunt ut laoreet dolore magna aliquam erat volutpat. Ut wisi enim ad minim veniam, quis nostrud exerci tation ullamcorper suscipit</p>
  <div class="abs" style="left:290px;top:92px;font-size:26px;color:#fff;font-family:Georgia,serif;font-weight:700">”</div>
  <p class="abs" style="left:213px;top:130px;font-size:5.5px;font-style:italic;color:#fff">- Lorem ipsum dolor</p>
  <p class="abs" style="left:13px;bottom:8px;font-size:4.5px;letter-spacing:2px;color:var(--red)">WWW.VORSTRUPKJAER.EXAMPLE</p>
  <div class="page-no">2</div>
</section>

<!-- 3 Our company -->
<section class="slide c3 r1">
  <h2 class="title red">OUR COMPANY</h2>
  <p class="abs body just" style="left:25px;top:48px;width:143px">Lorem ipsum dolor sit amet, consectetuer adipiscing elit, sed diam nonummy nibh euismod tincidunt ut laoreet dolore magna aliquam erat volutpat. Ut wisi enim ad minim veniam, quis nostrud exerci tation ullamcorper suscipit lorem ipsum dolor sit amet, consectetuer adipiscing elit, sed diam nonummy nibh euismod tincidunt ut laoreet dolore magna aliquam erat volutpat. Ut wisi enim ad minim veniam, quis nostrud exerci tation ullamcorper suscipit Lorem ipsum dolor sit amet, consectetuer adipiscing elit, sed diam nonummy nibh euismod tincidunt ut laoreet dolore magna aliquam erat volutpat.</p>
  <div class="photo" role="img" aria-label="Red map of Denmark with a location pin" style="left:230px;top:14px;width:110px;height:120px;background:radial-gradient(ellipse at 40% 50%,var(--red) 0%,var(--red) 45%,rgba(224,35,31,.15) 70%,transparent 75%)"></div>
  <div class="brand" style="left:25px;top:165px;font-size:6.5px"><span class="mark" style="width:13px;height:13px"></span><span>Vorstrup-Kjær<br>Consulting</span></div>
  <div class="abs" style="left:224px;top:161px;width:6px;height:16px;background:var(--red)"></div>
  <p class="abs" style="left:235px;top:161px;font-size:4.5px;line-height:1.5;font-style:italic;color:var(--ink)">Lorem ipsum dolorsit ,<br>No 12/456, 4th lane, Street, Road,<br>Denmark</p>
  <div class="page-no">3</div>
</section>

<!-- 4 Problem -->
<section class="slide c1 r2">
  <h2 class="title navy">UNDERSTANDING THE PROBLEM</h2>
  <div class="brand small"><span class="mark"></span><span>Vorstrup-Kjær<br>Consulting</span></div>
  <div class="card" style="left:26px;background:var(--ink)"><span class="icon"><svg width="16" height="16" viewBox="0 0 16 16" fill="none" stroke="#fff" stroke-width="1.2"><path d="M1 4h4l6 8h4M1 12h4l6-8h4M13 2l2 2-2 2M13 10l2 2-2 2"/></svg></span>Lorem ipsum dolor sit amet, consectetuer adipiscing elit, sed diam nonummy nibh euismod tincidunt ut laoreet dolore magna aliquam erat</div>
  <div class="card" style="left:135px;background:var(--mid)"><span class="icon"><svg width="16" height="16" viewBox="0 0 16 16" fill="none" stroke="#fff" stroke-width="1.2"><circle cx="8" cy="8" r="7"/><path d="M6 6a2 2 0 1 1 2 2v2M8 12v1"/></svg></span>Lorem ipsum dolor sit amet, consectetuer adipiscing elit, sed diam nonummy nibh euismod tincidunt ut laoreet dolore magna aliquam erat</div>
  <div class="card" style="left:244px;background:var(--light)"><span class="icon"><svg width="16" height="16" viewBox="0 0 16 16" fill="none" stroke="#333" stroke-width="1.2"><rect x="2" y="4" width="12" height="9"/><circle cx="8" cy="4" r="2"/><circle cx="14" cy="8.5" r="2"/></svg></span>Lorem ipsum dolor sit amet, consectetuer adipiscing elit, sed diam nonummy nibh euismod tincidunt ut laoreet dolore magna aliquam erat</div>
  <div class="page-no">4</div>
</section>

<!-- 5 Solutions -->
<section class="slide c2 r2">
  <h2 class="title red">OUR SOLUTIONS</h2>
  <div class="brand small"><span class="mark"></span><span>Vorstrup-Kjær<br>Consulting</span></div>
  <div class="card" style="left:26px;background:var(--navy)"><span class="icon"><svg width="16" height="16" viewBox="0 0 16 16" fill="none" stroke="#fff" stroke-width="1.2"><circle cx="8" cy="7" r="4"/><path d="M6 12h4M6.5 14h3M8 1v1M2 7h1M13 7h1"/></svg></span>Lorem ipsum dolor sit amet, consectetuer adipiscing elit, sed diam nonummy nibh euismod tincidunt ut laoreet dolore magna aliquam erat</div>
  <div class="card" style="left:135px;background:var(--red)"><span class="icon"><svg width="16" height="16" viewBox="0 0 16 16" fill="none" stroke="#fff" stroke-width="1.2"><rect x="2" y="3" width="12" height="10"/><circle cx="8" cy="8" r="2.5"/></svg></span>Lorem ipsum dolor sit amet, consectetuer adipiscing elit, sed diam nonummy nibh euismod tincidunt ut laoreet dolore magna aliquam erat</div>
  <div class="card" style="left:244px;background:var(--navy)"><span class="icon"><svg width="16" height="16" viewBox="0 0 16 16" fill="none" stroke="#fff" stroke-width="1.2"><path d="M4 12l-2 2M6 10c3-6 6-8 8-8 0 2-2 5-8 8zM5 7H2l2-2h3M9 11v3l2-2V9"/></svg></span>Lorem ipsum dolor sit amet, consectetuer adipiscing elit, sed diam nonummy nibh euismod tincidunt ut laoreet dolore magna aliquam erat</div>
  <div class="page-no">5</div>
</section>

<!-- 6 Process -->
<section class="slide c3 r2">
  <h2 class="title navy">OUR PROCESS &amp; GROWTH</h2>
  <div class="brand small"><span class="mark"></span><span>Vorstrup-Kjær<br>Consulting</span></div>
  <p class="abs body just" style="left:15px;top:60px;width:86px">Lorem ipsum dolor sit amet, consectetuer adipiscing elit, sed diam nonummy nibh euismod tincidunt ut laoreet dolore magna aliquam erat volutpat. Ut wisi enim ad minim veniam, quis nostrud exerci tation ullamcorper suscipit lorem ipsum dolor sit amet, consectetuer adipiscing elit, sed diam nonummy nibh euismod tincidunt ut laoreet dolore magna</p>
  <svg class="abs" style="left:120px;top:105px" width="226" height="14" viewBox="0 0 226 14">
    <line x1="4" y1="7" x2="222" y2="7" stroke="var(--ink)" stroke-width="1.5"/>
    <circle cx="25" cy="7" r="4.5" fill="var(--red)"/><circle cx="67" cy="7" r="4.5" fill="var(--navy)"/>
    <circle cx="111" cy="7" r="4.5" fill="var(--red)"/><circle cx="153" cy="7" r="4.5" fill="var(--navy)"/>
    <circle cx="197" cy="7" r="4.5" fill="var(--red)"/>
  </svg>
  <div class="step" style="left:122px;top:54px;background:var(--red)">STEP 1<svg width="18" height="18" viewBox="0 0 18 18" fill="none" stroke="#fff" stroke-width="1.3"><circle cx="9" cy="9" r="7"/><circle cx="9" cy="9" r="3"/></svg></div>
  <div class="step" style="left:208px;top:54px;background:var(--red)">STEP 3<svg width="18" height="18" viewBox="0 0 18 18" fill="none" stroke="#fff" stroke-width="1.3"><circle cx="9" cy="9" r="7"/><path d="M9 2v7h7"/></svg></div>
  <div class="step" style="left:294px;top:54px;background:var(--red)">STEP 5<svg width="18" height="18" viewBox="0 0 18 18" fill="none" stroke="#fff" stroke-width="1.3"><path d="M2 5h2l2 8h8l2-6H5"/><circle cx="7" cy="15.5" r="1"/><circle cx="13" cy="15.5" r="1"/></svg></div>
  <div class="step" style="left:164px;top:127px;background:var(--navy)">STEP 2<svg width="18" height="18" viewBox="0 0 18 18" fill="none" stroke="#fff" stroke-width="1.3"><rect x="2" y="2" width="12" height="10"/><path d="M8 8v8l2-2 2 3"/></svg></div>
  <div class="step" style="left:250px;top:127px;background:var(--navy)">STEP 4<svg width="18" height="18" viewBox="0 0 18 18" fill="none" stroke="#fff" stroke-width="1.3"><rect x="2" y="2" width="14" height="14"/><path d="M2 5h14"/><circle cx="9" cy="11" r="3"/></svg></div>
  <div class="page-no">6</div>
</section>

<!-- 7 Research -->
<section class="slide c1 r3">
  <div class="photo" role="img" aria-label="Dark photo of a desk with laptop and notes" style="inset:0;background:linear-gradient(120deg,#3a3a3a,#1f1f1f 60%,#2c2c2c)"></div>
  <h2 class="title white">OUR RESEARCH &amp; AGILITY</h2>
  <div class="brand small light"><span class="mark"></span><span>Vorstrup-Kjær<br>Consulting</span></div>
  <svg class="abs" style="left:41px;top:56px" width="52" height="52" viewBox="0 0 52 52" fill="none" stroke="#fff"><circle cx="26" cy="26" r="24" stroke-width="2.5"/><path d="M19 17h14v7a7 7 0 0 1-14 0zM19 19h-4a4 4 0 0 0 4 5M33 19h4a4 4 0 0 1-4 5M26 31v5M21 37h10" stroke-width="1.6"/></svg>
  <div class="abs" style="left:25px;top:118px;width:82px;height:7px;background:#fff;color:var(--ink);font-size:4.5px;letter-spacing:1.3px;text-align:center;line-height:7px;font-weight:600">EVOLUTION</div>
  <p class="abs" style="left:25px;top:138px;width:82px;height:48px;background:#fff;font-size:4px;line-height:1.9;text-align:center;padding:4px 5px;color:var(--ink)">Lorem ipsum dolor sit amet, consectetuer adipiscing elit, sed diam nonummy nibh euismod tincidunt ut laoreet dolore magna aliquam erat volutpat.</p>
  <svg class="abs" style="left:136px;top:58px" width="220" height="128" viewBox="0 0 220 128" font-family="Open Sans,sans-serif" font-size="4.2" fill="#fff">
    <text x="125" y="5" font-size="5" letter-spacing="1.2" text-anchor="middle" font-weight="600">CHART</text>
    <g stroke="#777" stroke-width=".4">
      <line x1="12" y1="119" x2="200" y2="119"/><line x1="12" y1="104" x2="200" y2="104"/><line x1="12" y1="88.5" x2="200" y2="88.5"/><line x1="12" y1="73" x2="200" y2="73"/><line x1="12" y1="57.5" x2="200" y2="57.5"/><line x1="12" y1="42" x2="200" y2="42"/><line x1="12" y1="26.5" x2="200" y2="26.5"/><line x1="12" y1="11" x2="200" y2="11"/>
    </g>
    <g text-anchor="end"><text x="8" y="121">0</text><text x="8" y="106">2</text><text x="8" y="90">4</text><text x="8" y="75">6</text><text x="8" y="59">8</text><text x="8" y="44">10</text><text x="8" y="28">12</text><text x="8" y="13">14</text></g>
    <rect x="63" y="85" width="18" height="34" fill="#fff"/><rect x="63" y="67" width="18" height="18" fill="#7a7a7a"/><rect x="63" y="52" width="18" height="15" fill="#a6a6a6"/>
    <rect x="109" y="100" width="18" height="19" fill="#fff"/><rect x="109" y="70" width="18" height="30" fill="#7a7a7a"/><rect x="109" y="50" width="18" height="20" fill="#a6a6a6"/>
    <rect x="155" y="93" width="18" height="26" fill="#fff"/><rect x="155" y="79" width="18" height="14" fill="#7a7a7a"/><rect x="155" y="56" width="18" height="23" fill="#a6a6a6"/>
    <rect x="200" y="84" width="18" height="35" fill="#fff"/><rect x="200" y="63" width="18" height="21" fill="#7a7a7a"/><rect x="200" y="18" width="18" height="45" fill="#a6a6a6"/>
    <g text-anchor="middle"><text x="72" y="126">Category 1</text><text x="118" y="126">Category 2</text><text x="164" y="126">Category 3</text><text x="209" y="126">Category 4</text></g>
  </svg>
  <div class="page-no">7</div>
</section>

<!-- 8 Target -->
<section class="slide c2 r3">
  <h2 class="title red">OUR TARGET</h2>
  <div class="brand small"><span class="mark"></span><span>Vorstrup-Kjær<br>Consulting</span></div>
  <p class="abs" style="left:11px;top:55px;font-family:'Titillium Web',sans-serif;font-weight:700;font-size:6px;letter-spacing:1.6px;color:var(--navy)">NEXT GENERATION TECHNOLOGY</p>
  <div class="photo" role="img" aria-label="Navy tinted photo of a person wearing a virtual reality headset" style="left:8px;top:70px;width:191px;height:111px;background:linear-gradient(90deg,#14183f 0%,#1f2466 55%,#3a3f7a 100%)"></div>
  <div class="abs" style="left:16px;top:76px;width:3px;height:99px;background:#fff"></div>
  <p class="abs" style="left:47px;top:82px;font-family:'Titillium Web',sans-serif;font-weight:700;font-size:11px;color:#fff;letter-spacing:1px">100 $</p>
  <p class="abs" style="left:52px;top:99px;font-size:4.3px;letter-spacing:1.6px;color:#fff;font-weight:600">AVERAGE</p>
  <div class="abs" style="left:34px;top:106px;width:53px;height:1px;background:#fff"></div>
  <p class="abs" style="left:55px;top:111px;font-size:4.3px;letter-spacing:1.4px;color:#fff;font-weight:600">AGE</p>
  <div class="abs" style="left:34px;top:120px;width:53px;height:11px;border:1px solid #fff;background:linear-gradient(90deg,#fff 30%,transparent 30%);color:var(--red);font-size:6px;line-height:9px;padding-left:16px">15 - 25</div>
  <div class="abs" style="left:34px;top:137px;width:53px;height:11px;border:1px solid #fff;background:linear-gradient(90deg,#fff 80%,transparent 80%);color:var(--red);font-size:6px;line-height:9px;padding-left:16px">26 - 35</div>
  <div class="abs" style="left:34px;top:154px;width:53px;height:11px;border:1px solid #fff;background:linear-gradient(90deg,#fff 55%,transparent 55%);color:var(--red);font-size:6px;line-height:9px;padding-left:16px">36 - 40</div>
  <svg class="abs" style="left:174px;top:158px" width="18" height="18" viewBox="0 0 18 18" fill="none" stroke="#fff" stroke-width="1.1"><rect x="3" y="3" width="12" height="12"/><circle cx="9" cy="9" r="3"/><path d="M6 1v2M9 1v2M12 1v2M6 15v2M9 15v2M12 15v2M1 6h2M1 12h2M15 6h2M15 12h2"/></svg>
  <p class="abs body just" style="left:219px;top:72px;width:124px;font-size:4.4px">Lorem ipsum dolor sit amet, consectetuer adipiscing elit, sed diam nonummy nibh euismod tincidunt ut laoreet dolore magna aliquam erat volutpat. Ut wisi enim ad minim veniam, quis nostrud exerci tation ullamcorper suscipit lorem ipsum dolor sit amet, consectetuer adipiscing elit, sed diam nonummy nibh euismod tincidunt ut laoreet dolore magna Lorem ipsum dolor sit amet, consectetuer adipiscing elit, sed diam nonummy nibh euismod tincidunt ut laoreet dolore magna aliquam erat volutpat. Ut wisi enim ad minim veniam, quis nostrud exerci tation ullamcorper</p>
  <div class="page-no">8</div>
</section>

<!-- 9 Consultants -->
<section class="slide c3 r3">
  <h2 class="title navy">OUR CONSULTANTS</h2>
  <div class="brand small"><span class="mark"></span><span>Vorstrup-Kjær<br>Consulting</span></div>
  <p class="abs" style="left:50px;top:49px;font-family:'Titillium Web',sans-serif;font-weight:700;font-size:6px;color:var(--navy)">LOREM IPSUM</p>
  <p class="abs" style="left:145px;top:49px;font-family:'Titillium Web',sans-serif;font-weight:700;font-size:6px;color:var(--red)">LOREM IPSUM</p>
  <p class="abs" style="left:239px;top:49px;font-family:'Titillium Web',sans-serif;font-weight:700;font-size:6px;color:var(--navy)">LOREM IPSUM</p>
  <div class="frame" style="left:49px;border:1px solid var(--red)"><div class="photo" role="img" aria-label="Portrait of a consultant" style="background:linear-gradient(180deg,#bdbdbd,#6f6f6f)"></div></div>
  <div class="frame" style="left:143px;border:1px solid var(--navy)"><div class="photo" role="img" aria-label="Portrait of a consultant" style="background:linear-gradient(180deg,#c9c9c9,#5e5e5e)"></div></div>
  <div class="frame" style="left:237px;border:1px solid var(--red)"><div class="photo" role="img" aria-label="Portrait of a consultant" style="background:linear-gradient(180deg,#f2f2f2,#9a9a9a)"></div></div>
  <svg class="abs" style="left:0;top:131px" width="362" height="16" viewBox="0 0 362 16" stroke="var(--ink)" stroke-width=".8"><path d="M84 0v14M80 11l4 4 4-4M178 0v14M174 11l4 4 4-4M272 0v14M268 11l4 4 4-4" fill="none"/></svg>
  <p class="abs" style="left:40px;top:152px;width:88px;font-size:4px;line-height:2;text-align:center;color:var(--ink)">Lorem ipsum dolor sit amet, consectetuer adipiscing elit, sed diam nonummy nibh euismod tincidunt ut laoreet dolore magna aliquam erat volutpat.</p>
  <p class="abs" style="left:134px;top:152px;width:88px;font-size:4px;line-height:2;text-align:center;color:var(--ink)">Lorem ipsum dolor sit amet, consectetuer adipiscing elit, sed diam nonummy nibh euismod tincidunt ut laoreet dolore magna aliquam erat volutpat.</p>
  <p class="abs" style="left:228px;top:152px;width:88px;font-size:4px;line-height:2;text-align:center;color:var(--ink)">Lorem ipsum dolor sit amet, consectetuer adipiscing elit, sed diam nonummy nibh euismod tincidunt ut laoreet dolore magna aliquam erat volutpat.</p>
  <div class="page-no">9</div>
</section>

<!-- 10 Partners -->
<section class="slide c1 r4">
  <div class="photo" role="img" aria-label="Faint grey world map in the background" style="left:30px;top:40px;width:330px;height:150px;background:radial-gradient(ellipse at 50% 45%,#e6e6e6 0%,#efefef 50%,#fff 75%)"></div>
  <h2 class="title red">OUR PARTNERS</h2>
  <div class="brand small"><span class="mark"></span><span>Vorstrup-Kjær<br>Consulting</span></div>
  <div class="abs" style="left:17px;top:57px;width:27px;height:27px;background:var(--red)"><svg width="27" height="27" viewBox="0 0 27 27" fill="none" stroke="#fff" stroke-width="1"><circle cx="13.5" cy="8" r="2.5"/><path d="M9 14h9M8 18a2 2 0 1 0 0 .1M13.5 18a2 2 0 1 0 0 .1M19 18a2 2 0 1 0 0 .1M13.5 11v3"/></svg></div>
  <div class="abs" style="left:17px;top:98px;width:27px;height:27px;background:var(--red)"><svg width="27" height="27" viewBox="0 0 27 27" fill="none" stroke="#fff" stroke-width="1"><circle cx="13.5" cy="7" r="2.5"/><circle cx="9" cy="15" r="2"/><circle cx="18" cy="15" r="2"/><path d="M6 21h15M13.5 10v3"/></svg></div>
  <div class="abs" style="left:17px;top:140px;width:27px;height:27px;background:var(--red)"><svg width="27" height="27" viewBox="0 0 27 27" fill="none" stroke="#fff" stroke-width="1"><rect x="7" y="5" width="13" height="6"/><circle cx="10" cy="16" r="2"/><circle cx="17" cy="16" r="2"/><path d="M6 22h15"/></svg></div>
  <p class="abs body" style="left:60px;top:57px;width:285px;font-size:4.4px">Lorem ipsum dolor sit amet, consectetuer adipiscing elit, sed diam nonummy nibh euismod tincidunt ut laoreet dolore magna aliquam erat volutpat. Ut wisi enim ad minim veniam, quis nostrud exerci tation ullamcorper suscipit lorem ipsum dolor sit amet, consectetuer adipiscing elit,</p>
  <p class="abs body" style="left:60px;top:99px;width:285px;font-size:4.4px">Lorem ipsum dolor sit amet, consectetuer adipiscing elit, sed diam nonummy nibh euismod tincidunt ut laoreet dolore magna aliquam erat volutpat. Ut wisi enim ad minim veniam, quis nostrud exerci tation ullamcorper suscipit lorem ipsum dolor sit amet, consectetuer adipiscing elit,</p>
  <p class="abs body" style="left:60px;top:141px;width:285px;font-size:4.4px">Lorem ipsum dolor sit amet, consectetuer adipiscing elit, sed diam nonummy nibh euismod tincidunt ut laoreet dolore magna aliquam erat volutpat. Ut wisi enim ad minim veniam, quis nostrud exerci tation ullamcorper suscipit lorem ipsum dolor sit amet, consectetuer adipiscing elit,</p>
  <div class="page-no">10</div>
</section>

<!-- 11 Goals -->
<section class="slide c2 r4">
  <h2 class="title navy">UPCOMING GOALS</h2>
  <div class="brand small"><span class="mark"></span><span>Vorstrup-Kjær<br>Consulting</span></div>
  <svg class="abs" style="left:75px;top:52px" width="20" height="22" viewBox="0 0 20 22" fill="none" stroke="var(--navy)" stroke-width="1.2"><path d="M10 1v3M8 3h4M7 6h6l-1 3h-4zM8 9l-2 9h8l-2-9M4 18h12v3H4z"/></svg>
  <div class="goal" style="left:60px;top:82px;width:49px;background:var(--red)">GOAL 1</div>
  <div class="goal" style="left:46px;top:105px;width:76px;background:var(--navy)">GOAL 2</div>
  <div class="goal" style="left:31px;top:127px;width:105px;background:var(--red)">GOAL 3</div>
  <div class="goal" style="left:17px;top:151px;width:134px;background:var(--navy)">GOAL 4</div>
  <svg class="abs" style="left:0;top:80px" width="362" height="90" viewBox="0 0 362 90" stroke="#888" stroke-width=".5"><path d="M109 8h13M122 31h13M136 53h13M151 77h13"/></svg>
  <p class="goal-text" style="left:124px;top:81px;width:225px">Lorem ipsum dolor sit amet, consectetuer adipiscing elit, sed diam nonummy nibh euismod tincidunt ut laoreet dolore magna aliquam erat volutpat.</p>
  <p class="goal-text" style="left:139px;top:104px;width:200px">Lorem ipsum dolor sit amet, consectetuer adipiscing elit, sed diam nonummy nibh euismod tincidunt ut laoreet dolore magna.</p>
  <p class="goal-text" style="left:153px;top:127px;width:185px">Lorem ipsum dolor sit amet, consectetuer adipiscing elit, sed diam nonummy nibh euismod tincidunt ut laoreet</p>
  <p class="goal-text" style="left:166px;top:150px;width:185px">Lorem ipsum dolor sit amet, consectetuer adipiscing elit, sed diam nonummy nibh euismod tincidunt ut laoreet</p>
  <div class="page-no">11</div>
</section>

<!-- 12 Contact -->
<section class="slide c3 r4">
  <div class="photo" role="img" aria-label="Light grey desk flat lay with phone, keyboard, notebook, pen and earphones" style="inset:0;background:linear-gradient(135deg,#e9e9e9 0%,#f4f4f4 45%,#dcdcdc 75%,#efefef 100%)"></div>
  <div class="brand" style="left:10px;top:100px;font-size:10px;gap:6px"><span class="mark" style="width:22px;height:22px"></span><span>Vorstrup-Kjær<br>Consulting</span></div>
  <div class="abs" style="left:10px;top:137px;border:1px solid var(--navy);padding:1px 4px;font-family:'Titillium Web',sans-serif;font-weight:700;font-size:6px;letter-spacing:2px;color:var(--navy)">GET IN TOUCH</div>
  <svg class="abs" style="left:18px;top:155px" width="10" height="42" viewBox="0 0 10 42" fill="none" stroke="var(--navy)" stroke-width=".9"><path d="M2 1h3l1 2-1.5 1.5a5 5 0 0 0 2 2L8 5l2 1v3c-5 0-8-3-8-8z"/><rect x="1" y="17" width="8" height="6"/><path d="M1 17l4 3 4-3"/><circle cx="5" cy="36" r="4"/><path d="M1 36h8M5 32c-2 2-2 6 0 8M5 32c2 2 2 6 0 8"/></svg>
  <p class="abs" style="left:31px;top:155px;font-size:4.5px;color:var(--red)">+123 456 7890</p>
  <p class="abs" style="left:32px;top:172px;font-size:4.5px;color:var(--red)">hello@vorstrupkjaer.example</p>
  <p class="abs" style="left:33px;top:187px;font-size:4.5px;color:var(--red)">www.vorstrupkjaer.example</p>
  <div class="socials" style="right:5px;bottom:6px"><span></span><span></span><span></span><span></span></div>
</section>

</body>
</html>
```